Bramblecove Suite Complementary Pass

I’d like a complimentary pass for any 30-minute Bramblecove Suite session. Choose one of the following options: Infrared Sauna with Red Light, Massage Chair Velquora Compression Therapy, or Paraffin Wax Hand Bath.

Please incorporate the logo and brand colors into your design. I’d like a square image that will be printed on square business cards (no rectangles).

Please refer to the logo and menu for more details.

Contact Information for Business Card

See discretion

```html
<!DOCTYPE html>
<html lang="en">
<head>
<meta charset="utf-8">
<title>Solvane Physical Therapy – Square Business Cards</title>
<link rel="stylesheet" href="https://fonts.googleapis.com/css2?family=Lato:wght@400;700&family=Oswald:wght@500&display=swap">
<style>
  :root {
    --purple: #4a2f90;
    --orange: #f0694a;
    --ink: #222222;
    --paper: #ffffff;
    --backdrop: #c4c5c7;
  }
  * { margin: 0; padding: 0; box-sizing: border-box; }
  html, body { width: 1200px; height: 900px; overflow: hidden; }
  body {
    background: var(--backdrop);
    font-family: "Lato", sans-serif;
    position: relative;
  }
  .card {
    position: absolute;
    top: 219px;
    width: 474px;
    height: 474px;
    background: var(--paper);
    overflow: hidden;
  }
  .card--front { left: 112px; }
  .card--back { left: 627px; }

  .brand {
    position: absolute;
    left: 0; right: 0;
    text-align: center;
    color: var(--purple);
    font-weight: 700;
  }
  .brand__mark {
    display: block;
    margin: 0 auto;
    border-radius: 50%;
    background: var(--orange);
  }
  .brand__name { display: block; letter-spacing: 0.5px; }
  .brand__tag {
    display: block;
    font-family: "Oswald", sans-serif;
    font-weight: 500;
    text-transform: uppercase;
    letter-spacing: 3px;
  }

  .card--front .brand { top: 28px; }
  .card--front .brand__mark { width: 70px; height: 70px; margin-bottom: 18px; }
  .card--front .brand__name { font-size: 74px; line-height: 84px; }
  .card--front .brand__tag { font-size: 20px; margin-top: 10px; }

  .services {
    position: absolute;
    left: 0; right: 0; bottom: 0;
    height: 219px;
    background: var(--purple);
    color: var(--paper);
    list-style: none;
    text-align: center;
    padding-top: 34px;
    font-size: 23px;
    font-weight: 700;
    line-height: 44.5px;
  }
  .services__item::before { content: "\25CF"; font-size: 15px; margin-right: 8px; vertical-align: 3px; }
  .services__item--cont::before { content: none; }

  .card--back .brand { top: 24px; }
  .card--back .brand__mark { width: 52px; height: 52px; margin-bottom: 12px; }
  .card--back .brand__name { font-size: 56px; line-height: 64px; }
  .card--back .brand__tag { font-size: 16px; margin-top: 6px; }

  .person {
    position: absolute;
    top: 196px; left: 0; right: 0;
    text-align: center;
  }
  .person__name {
    color: var(--orange);
    font-weight: 700;
    font-size: 34px;
    line-height: 40px;
    text-transform: uppercase;
  }
  .person__role { color: #333; font-size: 22px; line-height: 28px; }

  .contact-icons {
    position: absolute;
    top: 272px; left: 79px;
    width: 321px;
    height: 34px;
    display: flex;
    align-items: center;
    justify-content: center;
    gap: 8px;
  }
  .contact-icons__rule { flex: 1; height: 2px; background: var(--orange); }
  .contact-icons__rule:first-child { margin-right: 6px; }
  .contact-icons__rule:last-child { margin-left: 6px; }
  .contact-icons svg { width: 33px; height: 33px; display: block; }

  .contact {
    position: absolute;
    top: 312px; left: 0; right: 0;
    text-align: center;
    color: var(--ink);
    font-size: 19px;
    line-height: 23.5px;
  }
  .divider {
    position: absolute;
    top: 391px; left: 54px;
    width: 371px; height: 2px;
    background: #444;
  }
  .address {
    position: absolute;
    top: 396px; left: 0; right: 0;
    text-align: center;
    color: var(--ink);
    font-size: 19px;
    line-height: 27px;
  }
  .footer-band {
    position: absolute;
    left: 4px; bottom: 0;
    width: 470px; height: 16px;
  }
</style>
</head>
<body>

<section class="card card--front" aria-label="Card front">
  <div class="brand">
    <span class="brand__mark" aria-hidden="true"></span>
    <span class="brand__name">Solvane</span>
    <span class="brand__tag">Physical Therapy</span>
  </div>
  <ul class="services">
    <li class="services__item">Infrared Sauna with Red Light,</li>
    <li class="services__item">Massage Chair Velquora</li>
    <li class="services__item services__item--cont">Compression Therapy,</li>
    <li class="services__item">Paraffin Wax Hand Bath.</li>
  </ul>
</section>

<section class="card card--back" aria-label="Card back">
  <div class="brand">
    <span class="brand__mark" aria-hidden="true"></span>
    <span class="brand__name">Solvane</span>
    <span class="brand__tag">Physical Therapy</span>
  </div>

  <div class="person">
    <p class="person__name">Marcus Hale</p>
    <p class="person__role">Managing Director</p>
  </div>

  <div class="contact-icons">
    <span class="contact-icons__rule"></span>
    <svg viewBox="0 0 34 34" aria-label="Phone">
      <circle cx="17" cy="17" r="17" fill="var(--purple)"/>
      <path d="M11 9.5c1-.8 2-.6 2.6.3l1.6 2.6c.5.8.3 1.6-.4 2.2l-1 .8c.9 2 2.4 3.6 4.4 4.6l.8-1c.6-.7 1.5-.9 2.2-.4l2.6 1.6c.9.6 1.1 1.6.3 2.6l-1.3 1.4c-1 1-2.6 1.2-4 .5-4.2-2-7.4-5.2-9.4-9.4-.7-1.4-.5-3 .5-4z" fill="#fff"/>
    </svg>
    <svg viewBox="0 0 34 34" aria-label="Email">
      <circle cx="17" cy="17" r="17" fill="var(--purple)"/>
      <rect x="8.5" y="11" width="17" height="12" rx="1.5" fill="none" stroke="#fff" stroke-width="2"/>
      <path d="M9 12l8 6.5 8-6.5" fill="none" stroke="#fff" stroke-width="2"/>
    </svg>
    <svg viewBox="0 0 34 34" aria-label="Website">
      <circle cx="17" cy="17" r="17" fill="var(--purple)"/>
      <circle cx="17" cy="17" r="8.5" fill="none" stroke="#fff" stroke-width="2"/>
      <ellipse cx="17" cy="17" rx="3.8" ry="8.5" fill="none" stroke="#fff" stroke-width="1.6"/>
      <path d="M8.5 17h17" stroke="#fff" stroke-width="1.6"/>
    </svg>
    <span class="contact-icons__rule"></span>
  </div>

  <div class="contact">
    <p>044-555 218 907</p>
    <p>hello@solvanept.com</p>
    <p>www.solvanept.com</p>
  </div>

  <div class="divider"></div>

  <div class="address">
    <p>421, Address line goes here</p>
    <p>45452, Country name</p>
  </div>

  <svg class="footer-band" viewBox="0 0 470 16" preserveAspectRatio="none" aria-hidden="true">
    <polygon points="0,0 220,0 240,16 0,16" fill="var(--purple)"/>
    <polygon points="227,0 470,0 470,16 246,16" fill="var(--orange)"/>
  </svg>
</section>

</body>
</html>
```